Business Card Design Project

We need a business card design for a relatively new company called Lumen Stride. We design paddle (an outdoor winter sport primarily played in the midwest and east coast) and tennis bags for women and men. Lumen Stride is a lifestyle brand for the next generation country club goers. Our bags merge fashion with functionality and are making country club sports trendier and more fashionable.

I would like to include space for
Name: (will fill this in for employees)
Lumen Stride
Phone: (will do this)
Email:
www.lumenstride-example.net

Would also like to include Facebook and Twitter icons.
Please do not use pictures of the bags - this is just to give you an idea of what style bags we sell.

Target Market(s)

30 to 40 year old men and women - luxury market

Industry/Entity Type

Fashion

Requirements
Must have
• Would like the company logo included

```html
<!DOCTYPE html>
<html lang="en">
<head>
<meta charset="utf-8">
<title>Lumen Stride — Business Card</title>
<link rel="stylesheet" href="https://fonts.googleapis.com/css2?family=Jost:wght@300;400;500&display=swap">
<style>
  :root {
    --page: #e9e9eb;
    --card-light: #ededef;
    --band: #6e76a8;
    --band-line: #3f4f9c;
    --ink: #1a1a1e;
    --on-band: #ffffff;
    --title-ink: #1f2030;
  }
  * { box-sizing: border-box; margin: 0; padding: 0; }
  html, body { width: 1200px; height: 955px; overflow: hidden; }
  body {
    background: var(--page);
    font-family: "Jost", "Futura", sans-serif;
    position: relative;
  }
  .card {
    position: absolute;
    width: 540px;
    height: 310px;
    top: 322px;
    overflow: hidden;
    box-shadow: 0 6px 18px rgba(0,0,0,0.12);
  }
  .card--front { left: 40px; background: var(--card-light); }
  .card--back { left: 620px; background: var(--band); }

  .front__band {
    position: absolute;
    left: 0; right: 0; bottom: 0;
    height: 128px;
    background: var(--band);
    border-top: 3px solid var(--band-line);
  }
  .brand {
    position: absolute;
    display: flex;
    align-items: center;
    gap: 12px;
    color: var(--ink);
    font-weight: 300;
    letter-spacing: 0.5px;
  }
  .brand__dot {
    border-radius: 50%;
    background: var(--ink);
    flex: none;
  }
  .card--front .brand { left: 38px; top: 62px; font-size: 42px; }
  .card--front .brand__dot { width: 34px; height: 34px; }
  .card--back .brand { right: 44px; top: 130px; font-size: 38px; }
  .card--back .brand__dot { width: 30px; height: 30px; }

  .contact {
    position: absolute;
    right: 18px;
    top: 12px;
    list-style: none;
    color: var(--on-band);
    font-size: 11.5px;
    line-height: 15px;
    text-align: right;
    font-weight: 400;
  }
  .contact li { display: flex; justify-content: flex-end; align-items: center; gap: 7px; }
  .contact__mark {
    width: 10px; height: 10px;
    background: var(--ink);
    border: 1px solid var(--on-band);
    flex: none;
  }
  .person {
    position: absolute;
    left: 38px;
    bottom: 20px;
    display: flex;
    align-items: flex-start;
    gap: 10px;
  }
  .person__marker { margin-top: 4px; }
  .person__name { color: var(--on-band); font-size: 17px; font-weight: 500; line-height: 20px; }
  .person__title { color: var(--title-ink); font-size: 11px; line-height: 13px; }
</style>
</head>
<body>
  <section class="card card--front" aria-label="Business card front">
    <div class="brand"><span class="brand__dot"></span><span class="brand__name">Lumen Stride</span></div>
    <div class="front__band">
      <ul class="contact">
        <li>+123 555 0147 <span class="contact__mark"></span></li>
        <li>hello@lumenstride-example.net <span class="contact__mark"></span></li>
        <li>www.lumenstride-example.net <span class="contact__mark"></span></li>
        <li>facebook.com/LumenStride <span class="contact__mark"></span></li>
        <li>@LumenStride <span class="contact__mark"></span></li>
      </ul>
      <div class="person">
        <svg class="person__marker" width="12" height="12" viewBox="0 0 12 12" aria-hidden="true"><polygon points="0,12 12,0 12,12" fill="#1a1a1e"/></svg>
        <div>
          <p class="person__name">Dana Whitlow</p>
          <p class="person__title">President</p>
        </div>
      </div>
    </div>
  </section>

  <section class="card card--back" aria-label="Business card back">
    <div class="brand"><span class="brand__dot"></span><span class="brand__name">Lumen Stride</span></div>
  </section>
</body>
</html>
```